Life Coaching business needs a new flyer

We are an Australian business that specialises in Life Coaching, Career Coaching, Health and Wellness Coaching, Yoga and Pilates. We need a A4 double sided flyer that is full colour and folded to DL format. I have attached a couple of designs that I like and some pictures and would like the flyer to be bright yet stylish.

Life Coaching

```html
<!DOCTYPE html>
<html lang="en">
<head>
<meta charset="utf-8">
<title>Clearpath Coaching Flyer</title>
<link rel="stylesheet" href="https://fonts.googleapis.com/css2?family=Open+Sans:wght@400;600;700&display=swap">
<style>
:root{
  --bg:#d9d9d6;
  --paper:#f6f3dc;
  --paper-light:#fbf9ec;
  --brand-dot:#9a9a92;
  --ring:#4fae5a;
  --text:#3a3a3a;
  --contact:#4a68b0;
  --wave-light:#d6e79a;
  --wave-mid:#a9cf52;
  --wave-deep:#7fb52c;
}
*{margin:0;padding:0;box-sizing:border-box}
html,body{width:1200px;height:1000px;overflow:hidden;background:var(--bg)}
.stage{position:relative;width:1200px;height:1000px;font-family:"Open Sans",Arial,sans-serif;color:var(--text)}
.panel{position:absolute;top:110px;width:540px;height:760px;overflow:hidden;background:linear-gradient(180deg,var(--paper-light),var(--paper))}
.panel--cover{left:60px}
.panel--inside{left:600px}
.brand{position:absolute;display:flex;align-items:center;gap:10px;font-family:"Open Sans",Arial,sans-serif;font-weight:600;color:var(--text);line-height:1.25}
.brand-dot{flex:none;border-radius:50%;background:var(--brand-dot)}
.panel--cover .brand{left:290px;top:170px;width:235px;font-size:21px}
.panel--cover .brand-dot{width:18px;height:18px}
.panel--inside .brand{left:30px;top:140px;width:190px;font-size:14px}
.panel--inside .brand-dot{width:12px;height:12px}
.photo-circle{position:absolute;border-radius:50%;border:4px solid var(--ring)}
.photo-rect{position:absolute}
.contact{position:absolute;font-size:15px;line-height:1.45;color:var(--contact)}
.panel--cover .contact{left:45px;top:630px}
.panel--inside .contact{left:268px;top:605px;font-size:11.5px;line-height:1.4;opacity:.85}
.wave{position:absolute;left:0;top:0}
.heading{position:absolute;left:30px;top:196px;font-size:17px;font-weight:700;color:#333}
.column{position:absolute;font-size:10.6px;line-height:1.55}
.column--left{left:30px;top:236px;width:220px}
.column--right{left:265px;top:225px;width:240px;font-size:11.2px}
.quote{margin-bottom:10px}
.quote cite{display:block;font-style:normal}
.column p{margin-bottom:10px}
</style>
</head>
<body>
<div class="stage">

  <section class="panel panel--cover">
    <div class="brand"><span class="brand-dot"></span><span>Clearpath Coaching and Meditation Studio</span></div>

    <div class="photo-circle" role="img" aria-label="Signpost pointing to life balance, career, family, health and friends against a blue sky" style="left:25px;top:310px;width:210px;height:210px;background:radial-gradient(circle,#7fb4e6,#2d6fc0)"></div>
    <div class="photo-circle" role="img" aria-label="Woman in a yoga balance pose on a bright beach" style="left:245px;top:305px;width:132px;height:132px;background:linear-gradient(180deg,#8cc6ee,#f2f4f6)"></div>
    <div class="photo-circle" role="img" aria-label="Mother carrying her smiling daughter outdoors" style="left:420px;top:280px;width:165px;height:165px;background:radial-gradient(circle,#c89a78,#6f9a4a)"></div>
    <div class="photo-circle" role="img" aria-label="Cheerful group of colleagues celebrating" style="left:320px;top:420px;width:160px;height:160px;background:linear-gradient(180deg,#e9e9ea,#9aa6b6)"></div>
    <div class="photo-circle" role="img" aria-label="Group meditating outdoors on mats" style="left:410px;top:570px;width:112px;height:112px;background:linear-gradient(180deg,#8ec3ea,#6da34a)"></div>

    <div class="contact">
      Phone: 02 9000 4127<br>
      Email: hello@clearpathcoaching.com.au<br>
      www.clearpathcoaching.com.au
    </div>
  </section>

  <section class="panel panel--inside">
    <svg class="wave" width="540" height="760" viewBox="0 0 540 760" aria-hidden="true">
      <defs>
        <linearGradient id="waveGrad" x1="0" y1="0" x2="0" y2="1">
          <stop offset="0" stop-color="#a9cf52"/>
          <stop offset="1" stop-color="#7fb52c"/>
        </linearGradient>
      </defs>
      <path d="M0 640 C150 520 330 360 540 250 L540 760 L0 760 Z" fill="#d6e79a" opacity=".7"/>
      <path d="M0 700 C180 560 360 440 540 380 L540 760 L0 760 Z" fill="url(#waveGrad)" opacity=".8"/>
      <path d="M0 560 C200 470 380 330 540 290" fill="none" stroke="#ffffff" stroke-width="3" opacity=".6"/>
    </svg>

    <div class="photo-rect" role="img" aria-label="Woman cheering beside a pink car under a blue sky" style="left:205px;top:0;width:85px;height:130px;background:linear-gradient(180deg,#6fb6e8,#e0739c)"></div>
    <div class="photo-rect" role="img" aria-label="Hiker resting before snowy mountains and a lake" style="left:290px;top:0;width:108px;height:155px;background:linear-gradient(180deg,#7aa6d6,#c9d6de 55%,#6f7f74)"></div>
    <div class="photo-rect" role="img" aria-label="Mother giving her daughter a piggyback in a sunny park" style="left:398px;top:0;width:135px;height:190px;background:linear-gradient(180deg,#e8c49a,#7aa548)"></div>

    <div class="brand"><span class="brand-dot"></span><span>Clearpath Coaching</span></div>

    <h2 class="heading">Happy Clients Testimonials</h2>

    <div class="column column--left">
      <div class="quote">“I have lost 10 kilos and now have the energy to play with my kids. Thanks Mara for your support/guidance and helping me get rid of my limiting beliefs. I feel I can achieve anything now! The sky’s the limit”<cite>Erin, Mosman</cite></div>
      <div class="quote">“I had always wanted to start up own café however every time it came to putting it into practice I would procrastinate and not achieve anything. I became overwhelmed with the whole process and never achieved anything. Mara put it into bite sized chunks and helped me to set small achievable goals. I am now a happy café owner.”<cite>Tessa, Double Bay</cite></div>
      <div class="quote">“Mara has helped to change my life around in all aspects. I would have been lost without her. Thanks Mara for your professionalism, support and guidance.”<cite>Chloe, Cremorne</cite></div>
      <div class="quote">“I was so busy with kids, work, and my husband I lost who I was. Mara has helped me find the person I am again.”<cite>Megan, Chatswood</cite></div>
    </div>

    <div class="column column--right">
      <div class="quote">“When I started with Coach Mara, I didn’t know anything about coaching. I called her because she helped a friend of mine make a career change that was a perfect fit for her. I had the opportunity to make a change too and did not know where to start. I am now in a job that I love. I would recommend Mara to everyone.”<cite>Owen, Texas America</cite></div>
      <p>Clearpath Coaching and Meditation Studio is a professional service that can help you achieve the goals that you are looking for in Life Coaching, Meditation, and Yoga/Pilates.</p>
      <p>If you are ready to take your life to the next level and would like to know more, please contact us.</p>
    </div>

    <div class="contact">
      Phone: 02 9000 4127<br>
      Email: hello@clearpathcoaching.com.au<br>
      www.clearpathcoaching.com.au
    </div>
  </section>

</div>
</body>
</html>
```